Financial Planning Business needs a business card design

We need a business card design that is for a new financial planning business based in Australia. We provide financial planning advice such as retirement planning, wealth creation, asset protection.

Attached is the logo design. On the front side of the business card needs to incorporate the following:
- adviser name
- adviser title (ie Managing Director)
- address
- phone number
- email
- website address

Ideally it should also have the business name and logo

On the back of the card I would like this to be black in colour with the business name and logo

I have been advised the font is "Cinzel" (regular and bold)

Industry/Entity Type

Financial

Requirements
Must have
• Logo and business name

Format to have as follows:
Ben xxxxxxxx
Managing Director / Senior Financial Adviser
address
phone email
website

```html
<!DOCTYPE html>
<html lang="en">
<head>
<meta charset="utf-8">
<title>Keystone Wealth Planning – Business Card</title>
<link href="https://fonts.googleapis.com/css2?family=Cinzel:wght@400;700&family=Open+Sans:wght@400&display=swap" rel="stylesheet">
<style>
  :root {
    --page-bg: #e8e5e0;
    --card-white: #ffffff;
    --brand-blue: #0b9bd0;
    --swoosh-dark: #2f2f31;
    --ink-grey: #3a3a3a;
    --back-grey: #9a9a9a;
    --on-dark: #ffffff;
    --divider: #d9d9d9;
  }
  * { margin: 0; padding: 0; box-sizing: border-box; }
  html, body {
    width: 1200px; height: 1157px; overflow: hidden;
    background: var(--page-bg);
  }
  .canvas { position: relative; width: 1200px; height: 1157px; }

  .card {
    position: absolute;
    width: 906px; height: 516px;
    border-radius: 22px;
    overflow: hidden;
  }
  .card-front { left: 32px; top: 40px; background: var(--card-white); box-shadow: 0 2px 6px rgba(0,0,0,.15); }
  .card-back  { left: 248px; top: 584px; background: var(--back-grey); box-shadow: 0 2px 6px rgba(0,0,0,.15); }

  .wave { position: absolute; left: 0; top: 0; width: 906px; height: 516px; }

  .brand {
    position: absolute; left: 68px; top: 44px;
    display: flex; align-items: center; gap: 22px;
  }
  .brand-square { width: 86px; height: 86px; background: var(--brand-blue); }
  .brand-name {
    font-family: "Cinzel", serif; font-weight: 400;
    color: var(--brand-blue);
    font-size: 46px; line-height: 52px;
  }

  .adviser {
    position: absolute; left: 70px; top: 214px;
    font-family: "Cinzel", serif; font-size: 32px; letter-spacing: .5px;
  }
  .adviser-name { color: var(--brand-blue); font-weight: 700; }
  .adviser-title { color: var(--ink-grey); font-weight: 400; }

  .contacts {
    position: absolute; left: 68px; top: 364px;
    list-style: none;
    font-family: "Open Sans", sans-serif; font-size: 21px; color: var(--on-dark);
  }
  .contacts li { display: flex; align-items: center; height: 35px; }
  .contacts svg { width: 20px; height: 20px; margin-right: 9px; fill: var(--on-dark); }

  .divider {
    position: absolute; left: 462px; top: 438px;
    width: 2px; height: 64px; background: var(--divider);
  }
  .address {
    position: absolute; left: 482px; top: 440px;
    font-family: "Open Sans", sans-serif; font-size: 20px; line-height: 32px;
    color: var(--on-dark);
  }

  .back-brand {
    position: absolute; left: 0; top: 150px; width: 100%;
    text-align: center;
    font-family: "Cinzel", serif; font-weight: 400;
    font-size: 54px; line-height: 66px; color: var(--on-dark);
  }
  .back-url {
    position: absolute; left: 0; top: 438px; width: 100%;
    text-align: center;
    font-family: "Open Sans", sans-serif; font-size: 28px; letter-spacing: 2.6px;
    color: var(--on-dark);
  }
</style>
</head>
<body>
<main class="canvas">

  <section class="card card-front">
    <svg class="wave" viewBox="0 0 906 516" aria-hidden="true">
      <path fill="var(--swoosh-dark)" d="M0,306 C150,256 310,286 480,348 C640,406 790,440 906,392 L906,400 C790,452 640,426 480,370 C320,314 150,296 0,336 Z"/>
      <path fill="var(--brand-blue)" d="M0,342 C150,298 310,322 480,384 C640,440 790,448 906,398 L906,516 L0,516 Z"/>
    </svg>

    <div class="brand">
      <span class="brand-square"></span>
      <div class="brand-name">Keystone<br>Wealth Planning</div>
    </div>

    <h1 class="adviser"><span class="adviser-name">Your Name,</span> <span class="adviser-title">Title</span></h1>

    <ul class="contacts">
      <li>
        <svg viewBox="0 0 20 20"><circle cx="10" cy="10" r="9" fill="none" stroke="#fff" stroke-width="2"/><path d="M6.5 5.5l2 0 1 3-1.5 1c.8 1.5 1.5 2.2 3 3l1-1.5 3 1v2c-4 .5-9-4.5-8.5-8.5z"/></svg>
        012-345-6789
      </li>
      <li>
        <svg viewBox="0 0 20 20"><rect x="5" y="3" width="10" height="6"/><rect x="1" y="9" width="18" height="8" rx="1.5"/></svg>
        012-345-6789
      </li>
      <li>
        <svg viewBox="0 0 20 20"><path d="M2 7l8-4 8 4v10H2z"/><path d="M3 8l7 5 7-5" fill="none" stroke="#0b9bd0" stroke-width="1.5"/></svg>
        info@keystonewealthplanning.com
      </li>
      <li>
        <svg viewBox="0 0 20 20"><circle cx="10" cy="10" r="9"/><g fill="none" stroke="#0b9bd0" stroke-width="1.2"><ellipse cx="10" cy="10" rx="4" ry="8.5"/><path d="M1.5 10h17M3 6h14M3 14h14M10 1.5v17"/></g></svg>
        www.keystonewealthplanning.com
      </li>
    </ul>

    <span class="divider"></span>
    <address class="address" style="font-style:normal">Sreet Name, City Name<br>Zip Code-00000</address>
  </section>

  <section class="card card-back">
    <div class="back-brand">Keystone<br>Wealth Planning</div>
    <div class="back-url">www.keystonewealthplanning.com</div>
  </section>

</main>
</body>
</html>
```